Engineering group involved with fire safety needs a business card

We need a business card design for a company based in Greece called "Varotis Group". We are engineers and specialized technicians, operating the following : a) Fire fighting equipment trade b) Installation , Inspection & Maintenance of fire extinguishers and fire protection systems c) Occupational Health & Safety (Risk assessment & management/ Staff training). We need a clear and simple card design. I uploaded a draft I made, in order to give you an idea of the company and how I currently imagine the design of the card. I also uploaded the logo in .png file format. We are always open to different, new suggestions and ideas you may want to submit.
Target Market(s)
industries, companies, managers, retail clients
Industry/Entity Type
Fire Safety
Contact Information for Business Card
Addresses & phone numbers (headquarters + branch), logo, name (you can find all the details on the uploaded files!)
Colors
Designer to choose colors to be used in the design.
Look and feel
Each slider illustrates characteristics of the customer's brand and the style your logo design should communicate.

```html
<!DOCTYPE html>
<html lang="en">
<head>
<meta charset="utf-8">
<title>Varotis Group – Business Card</title>
<link href="https://fonts.googleapis.com/css2?family=Source+Sans+3:wght@400;700&display=swap" rel="stylesheet">
<style>
  :root {
    --page: #ffffff;
    --card-light: #ffffff;
    --card-dark: #464c4f;
    --brand-red: #a8151f;
    --ink: #2b2b2b;
    --ink-soft: #333333;
    --on-dark: #ffffff;
    --edge: #555555;
  }
  html, body {
    margin: 0; padding: 0;
    width: 1200px; height: 1200px;
    overflow: hidden;
    background: var(--page);
    font-family: "Source Sans 3", sans-serif;
  }
  .canvas { position: relative; width: 1200px; height: 1200px; }
  .card {
    position: absolute; top: 277px;
    width: 415px; height: 681px;
    box-sizing: border-box;
    box-shadow: 14px 14px 18px rgba(0,0,0,0.12);
  }
  .card--front { left: 164px; background: var(--card-light); border: 1px solid var(--edge); color: var(--ink); }
  .card--back { left: 615px; background: var(--card-dark); color: var(--on-dark); }

  .brand {
    position: absolute; top: 110px; left: 0; right: 0;
    display: flex; align-items: center; justify-content: center; gap: 10px;
  }
  .brand__mark { width: 22px; height: 22px; background: var(--brand-red); }
  .card--back .brand__mark { background: var(--on-dark); }
  .brand__name {
    font-weight: 700; font-size: 38px; letter-spacing: 1px;
    color: var(--brand-red); white-space: nowrap;
  }
  .card--back .brand__name { color: var(--on-dark); }

  .tagline {
    position: absolute; top: 202px; left: 0; right: 0;
    text-align: center; font-size: 20.5px; white-space: nowrap;
  }
  .person { position: absolute; top: 255px; left: 0; right: 0; text-align: center; }
  .person__name { font-weight: 700; font-size: 22px; color: var(--ink-soft); line-height: 30px; }
  .person__role { font-size: 19.5px; color: var(--brand-red); line-height: 26px; }

  .accent-bar {
    position: absolute; left: 0; top: 365px;
    width: 14px; height: 113px; background: var(--brand-red);
  }
  .contact-list, .service-list {
    position: absolute; top: 358px; left: 30px;
    margin: 0; padding: 0; list-style: none;
    font-size: 23px; line-height: 32px; white-space: nowrap;
  }
  .offices {
    position: absolute; top: 519px; left: 30px;
    font-size: 19.5px; line-height: 22px;
  }
  .offices p { margin: 0 0 4px; }
  .website {
    position: absolute; top: 632px; left: 0; right: 0;
    text-align: center; font-size: 19.5px; color: var(--brand-red);
  }
  .back-links {
    position: absolute; top: 603px; left: 0; right: 0;
    text-align: center; font-size: 19.5px; line-height: 27px;
  }
</style>
</head>
<body>
<div class="canvas">

  <section class="card card--front">
    <div class="brand"><span class="brand__mark"></span><span class="brand__name">VAROTIS GROUP</span></div>
    <div class="tagline">installation • inspection • maintenance</div>
    <div class="person">
      <div class="person__name">NIKOLAOS VAROTIS</div>
      <div class="person__role">Mechanical Engineer</div>
      <div class="person__role">OHS Consultant</div>
    </div>
    <div class="accent-bar"></div>
    <ul class="contact-list">
      <li>Tel. (HQ) +30 22920 41583</li>
      <li>Tel. (BO) +30 210 6172940</li>
      <li>Mob. +30 694 215 37 80</li>
      <li>nikolaos.varotis@varotisgroup.gr</li>
    </ul>
    <div class="offices">
      <p>Headquarters:<br>12 Anemonis Street, 19500 Lavrio</p>
      <p>Branch Office:<br>45 Kyprou Avenue, 15124 Marousi</p>
    </div>
    <div class="website">www.varotisgroup.gr</div>
  </section>

  <section class="card card--back">
    <div class="brand"><span class="brand__mark"></span><span class="brand__name">VAROTIS GROUP</span></div>
    <div class="tagline">installation • inspection • maintenance</div>
    <div class="accent-bar"></div>
    <ul class="service-list">
      <li>Fire Fighting Equipment</li>
      <li>licensing &amp; Business Registration</li>
      <li>Occupational Health &amp; Safety</li>
      <li>Staff Training</li>
    </ul>
    <div class="back-links">
      info@varotisgroup.gr<br>www.varotisgroup.gr
    </div>
  </section>

</div>
</body>
</html>
```